Website Design for Kindred Harbor Network

Please design and code a new website.
Here are the sites I like best:
http://www.voyaglint.com/alternate/
http://www.wheelsbrevant.org
Please make it similar but look at the competitor site (below) for images and wording. This is NOT a car donation site. It's a senior lead placement site like https://www.elderbrookhaven.com. I just like this sites above as a lead generation sites.
Competitor site:
https://www.elderbrookhaven.com (use ideas / verbiage from this site)
Updates
Competitor site:

```html
<!DOCTYPE html>
<html lang="en">
<head>
<meta charset="utf-8">
<title>Kindred Harbor Network – Senior Living Near You</title>
<link href="https://fonts.googleapis.com/css2?family=Montserrat:wght@400;500;600;700;800&family=Open+Sans:wght@400;600;700&display=swap" rel="stylesheet">
<style>
:root{
  --navy:#0c2b5e;
  --navy-deep:#082149;
  --green:#22c58a;
  --green-dark:#13915f;
  --ink:#1d2433;
  --muted:#4b5363;
  --line:#dfe4ea;
  --pale-blue:#f3f7fd;
  --pale-gray:#eceff2;
  --white:#ffffff;
}
*{box-sizing:border-box;margin:0;padding:0}
html,body{width:1200px;height:4571px;overflow:hidden;background:var(--white)}
body{font-family:"Open Sans",Arial,sans-serif;color:var(--ink)}
.page{position:relative;width:1200px;height:4571px;overflow:hidden}
.abs{position:absolute}
h1,h2,h3,.heading{font-family:"Montserrat",Arial,sans-serif}
.accent{color:var(--green)}

/* header */
.site-header{left:0;top:0;width:1200px;height:144px}
.brand{left:40px;top:42px;display:flex;align-items:center;gap:14px}
.brand-dot{width:40px;height:40px;border-radius:50%;background:var(--green);flex:none}
.brand-name{font-family:"Montserrat",sans-serif;font-weight:700;font-size:24px;color:var(--navy);white-space:nowrap}
.brand-tag{left:94px;top:86px;font-size:11px;letter-spacing:.5px;color:#7b8493;font-family:"Montserrat",sans-serif}
.header-phone{left:806px;top:40px;display:flex;align-items:center;gap:14px}
.phone-ring{width:56px;height:56px;border:3px solid var(--navy);border-radius:50%;display:flex;align-items:center;justify-content:center;flex:none}
.phone-number{font-family:"Montserrat",sans-serif;font-weight:800;font-size:29px;color:var(--navy);line-height:1;white-space:nowrap}
.phone-note{font-size:11.5px;color:var(--navy);margin-top:4px;white-space:nowrap}

/* nav */
.main-nav{left:16px;top:144px;width:761px;height:55px;background:var(--navy);display:flex;align-items:center;padding-left:20px;gap:18px}
.nav-home{width:32px;height:32px;background:var(--green);display:flex;align-items:center;justify-content:center;flex:none}
.nav-link{font-family:"Montserrat",sans-serif;font-weight:700;font-size:11.5px;color:var(--white);letter-spacing:.1px;white-space:nowrap}
.nav-tail{left:777px;top:144px;width:407px;height:55px;background:var(--navy)}

/* hero */
.hero-photo{left:16px;top:199px;width:1168px;height:503px;background:linear-gradient(100deg,#6f7b4d 0%,#8a9462 30%,#a8a98a 55%,#b7b7a8 75%,#8c8a83 100%)}
.hero-title{left:40px;top:384px;width:680px;text-align:center;font-family:"Montserrat",sans-serif;font-weight:700;font-size:37px;line-height:48px;color:var(--white);text-shadow:0 2px 8px rgba(0,0,0,.35)}

/* contact form */
.contact-panel{left:777px;top:126px;width:407px;height:429px;background:var(--navy)}
.contact-head{height:73px;background:var(--green);display:flex;align-items:center;justify-content:center;font-family:"Montserrat",sans-serif;font-weight:700;font-size:27px;color:var(--white)}
.field{position:absolute;height:47px;background:var(--white);font-size:13px;font-weight:600;color:var(--ink);padding:0 12px;display:flex;align-items:center}
.field .req{color:#d23b3b}
.field-select{justify-content:space-between;padding-right:0}
.select-arrow{width:40px;height:100%;border-left:1px solid var(--line);display:flex;align-items:center;justify-content:center}
.submit-btn{position:absolute;left:23px;top:345px;width:137px;height:43px;background:var(--green);color:var(--white);font-family:"Montserrat",sans-serif;font-weight:700;font-size:13px;display:flex;align-items:center;justify-content:center;letter-spacing:.5px}

/* support strip */
.support-strip{left:16px;top:702px;width:1168px;height:194px;background:linear-gradient(180deg,#f1f2f3,#e4e6e8)}
.support-label{left:16px;top:674px;width:487px;height:222px}
.support-text{left:62px;top:722px;font-family:"Montserrat",sans-serif;font-weight:700;color:var(--white);font-size:30px;line-height:38px;white-space:nowrap}
.support-text .big{font-size:40px;line-height:50px}
.feature{top:736px;width:130px;text-align:center}
.feature svg{display:block;margin:0 auto}
.feature p{margin-top:10px;font-size:11.5px;font-weight:600;line-height:14px;color:var(--ink)}

/* how it works */
.section-title{font-family:"Montserrat",sans-serif;font-weight:700;color:var(--navy)}
.how-title{left:0;top:986px;width:1200px;text-align:center;font-size:33px;padding-right:380px}
.step{top:1076px;width:180px;text-align:center}
.step-photo{width:142px;height:142px;border-radius:50%;margin:0 auto;border:6px solid #f1f3f6;box-shadow:0 4px 12px rgba(0,0,0,.08)}
.step-num{margin-top:30px;font-family:"Montserrat",sans-serif;font-weight:600;font-size:25px;color:var(--navy)}
.step.alt .step-num{color:var(--green)}
.step-text{margin-top:6px;font-size:16.5px;line-height:27px;color:var(--ink)}
.couple-photo{left:834px;top:994px;width:350px;height:453px;background:linear-gradient(180deg,#ffffff 0%,#e8eef4 40%,#c9d3dc 75%,#b3a28a 100%)}

/* no cost */
.nocost-band{left:16px;top:1447px;width:1168px;height:441px;background:linear-gradient(100deg,#6f9fd6 0%,#a7c6ea 35%,#d8e7f7 70%,#e9f2fb 100%)}
.nocost-title{left:620px;top:1530px;width:560px;text-align:center;font-size:38px}
.nocost-text{left:690px;top:1615px;width:420px;text-align:center;font-weight:700;font-size:17px;line-height:25px;color:var(--ink)}
.btn-call{left:727px;top:1719px;width:347px;height:64px;background:var(--green);color:var(--white);font-family:"Montserrat",sans-serif;font-weight:700;font-size:32px;display:flex;align-items:center;justify-content:center;border-radius:4px}

/* veterans */
.vet-title{left:96px;top:1980px;font-size:29px}
.vet-text{left:96px;top:2064px;width:560px;font-size:16.5px;line-height:27px;color:var(--ink)}
.btn-learn{left:96px;top:2224px;width:208px;height:41px;background:var(--green-dark);color:var(--white);font-family:"Montserrat",sans-serif;font-weight:600;font-size:15px;display:flex;align-items:center;justify-content:center;border-radius:3px}
.vet-photo{left:811px;top:1989px;width:298px;height:274px;border-radius:50%;border:8px solid #f1f3f6;background:linear-gradient(135deg,#1b2c52 0%,#41577f 45%,#b23a44 70%,#e7e3e8 100%);box-shadow:0 6px 16px rgba(0,0,0,.12)}

/* testimonials */
.reviews-band{left:16px;top:2355px;width:1168px;height:708px;background:var(--pale-blue)}
.reviews-title{left:0;top:2448px;width:1200px;text-align:center;font-size:31px}
.quote{position:absolute;padding:30px 34px;font-size:14.5px;line-height:25px;color:#333a48}
.quote-a{left:91px;top:2531px;width:515px;height:171px;background:#f0edfb}
.quote-b{left:590px;top:2583px;width:519px;height:183px;background:#ebf9f6}
.reviewer{display:flex;align-items:center;gap:18px}
.avatar{width:90px;height:90px;border-radius:50%;border:5px solid var(--white);background:linear-gradient(160deg,#d9b79a,#9b7a62);box-shadow:0 3px 10px rgba(0,0,0,.12)}
.reviewer-name{font-family:"Open Sans",sans-serif;font-style:italic;font-weight:600;font-size:18px;color:var(--ink)}
.dots{left:0;top:2958px;width:1200px;display:flex;justify-content:center;gap:6px}
.dots span{width:12px;height:12px;border-radius:50%;border:1.5px solid #c5cbd4;background:var(--white)}
.dots span.on{background:#c5cbd4}

/* local advisor */
.advisor-photo{left:16px;top:3063px;width:1168px;height:494px;background:linear-gradient(90deg,#eeeff0 0%,#eceae8 40%,#e4d6cb 62%,#d2b7a0 80%,#c79e84 100%)}
.advisor-title{left:86px;top:3156px;font-size:31px;line-height:41px}
.advisor-text{left:86px;top:3255px;width:470px;font-size:17.5px;line-height:28px;color:var(--ink)}
.advisor-list{left:82px;top:3342px;list-style:none}
.advisor-list li{display:flex;align-items:center;gap:16px;height:43px;font-family:"Montserrat",sans-serif;font-weight:500;font-size:17px;color:var(--navy)}

/* states */
.states-title{left:0;top:3648px;width:1200px;text-align:center;font-size:33px}
.care-tab{position:absolute;left:91px;width:275px;height:46px;background:var(--white);box-shadow:0 2px 8px rgba(0,0,0,.1);display:flex;align-items:center;gap:18px;font-family:"Montserrat",sans-serif;font-weight:500;font-size:16px;color:var(--navy)}
.care-tab .tab-icon{width:46px;height:46px;background:var(--navy);display:flex;align-items:center;justify-content:center}
.care-tab.active{color:var(--green)}
.care-tab.active .tab-icon{background:var(--green)}
.care-tab .tab-caret{margin-left:auto;margin-right:14px}
.state-col{position:absolute;top:3734px;list-style:none;font-size:14px;line-height:22.6px;color:#2a3140}

/* footer */
.footer-band{left:16px;top:4206px;width:1168px;height:309px;background:var(--pale-gray)}
.footer-photo{left:34px;top:4160px;width:240px;height:355px;background:linear-gradient(180deg,#dcdde0 0%,#c6c1bc 40%,#6f7888 75%,#4b5567 100%)}
.footer-heading{font-family:"Montserrat",sans-serif;font-weight:700;font-size:13px;color:var(--green-dark);letter-spacing:.3px}
.footer-about{left:297px;top:4286px;width:280px}
.footer-about p{margin-top:26px;font-size:12.5px;line-height:19px;color:var(--ink)}
.footer-links{left:622px;top:4286px}
.footer-links ul{list-style:none;margin-top:26px;font-size:12.5px;line-height:19.5px;color:var(--ink)}
.footer-panel{left:846px;top:4211px;width:338px;height:304px}
.footer-brand{left:884px;top:4262px;display:flex;align-items:center;gap:12px}
.footer-brand .brand-dot{width:32px;height:32px}
.footer-brand .brand-name{color:var(--white);font-size:17px}
.footer-phone{left:890px;top:4390px;display:flex;align-items:center;gap:12px;color:var(--white)}
.footer-phone .phone-ring{border-color:var(--white);width:48px;height:48px}
.footer-phone .phone-number{color:var(--white);font-size:25px}
.footer-phone .phone-note{color:var(--white);font-size:10.5px}
.copyright{left:0;top:4534px;width:1200px;text-align:center;font-family:"Montserrat",sans-serif;font-weight:600;font-size:11px;color:var(--ink);letter-spacing:.3px}
</style>
</head>
<body>
<div class="page">

  <header class="abs site-header">
    <div class="abs brand"><span class="brand-dot"></span><span class="brand-name">Kindred Harbor Network</span></div>
    <div class="abs brand-tag">CONNECTING FAMILIES TO SENIOR LIVING</div>
    <div class="abs header-phone">
      <span class="phone-ring">
        <svg width="26" height="26" viewBox="0 0 24 24"><path d="M6.6 10.8a15 15 0 0 0 6.6 6.6l2.2-2.2a1 1 0 0 1 1-.25 11.4 11.4 0 0 0 3.6.57 1 1 0 0 1 1 1V20a1 1 0 0 1-1 1A17 17 0 0 1 3 4a1 1 0 0 1 1-1h3.5a1 1 0 0 1 1 1c0 1.25.2 2.450.57 3.57a1 1 0 0 1-.25 1z" fill="#0c2b5e"/></svg>
      </span>
      <div><div class="phone-number">1-800-555-0142</div><div class="phone-note">Talk Today to a Local Advisor for FREE</div></div>
    </div>
  </header>

  <nav class="abs main-nav">
    <span class="nav-home"><svg width="18" height="16" viewBox="0 0 18 16"><path d="M9 1 1 8h2.5v7h4v-5h3v5h4V8H17z" fill="#fff"/></svg></span>
    <span class="nav-link">ASSISTED LIVING</span>
    <span class="nav-link">MEMORY CARE</span>
    <span class="nav-link">NURSING HOMES</span>
    <span class="nav-link">MORE LIVING OPTIONS ▾</span>
    <span class="nav-link">PLANNING &amp; ADVICE</span>
  </nav>
  <div class="abs nav-tail"></div>

  <div class="abs hero-photo" role="img" aria-label="Photo of an adult daughter walking arm in arm with her elderly father along a sunny garden path"></div>
  <h1 class="abs hero-title">You know your family.<br>We know Senior Living.<br>Find Senior Living Near You.</h1>

  <form class="abs contact-panel">
    <div class="contact-head">Contact us now!</div>
    <div class="field" style="left:23px;top:105px;width:155px">First Name<span class="req">*</span></div>
    <div class="field" style="left:190px;top:105px;width:153px">Last Name<span class="req">*</span></div>
    <div class="field" style="left:23px;top:164px;width:155px">Primary Phone<span class="req">*</span></div>
    <div class="field" style="left:190px;top:164px;width:153px">Cell Phone<span class="req">*</span></div>
    <div class="field" style="left:23px;top:224px;width:320px">Email Address<span class="req">*</span></div>
    <div class="field field-select" style="left:23px;top:283px;width:320px"><span>State<span class="req">*</span></span><span class="select-arrow"><svg width="14" height="9" viewBox="0 0 14 9"><path d="M0 0h14L7 9z" fill="#555"/></svg></span></div>
    <div class="submit-btn">SUBMIT</div>
  </form>

  <div class="abs support-strip"></div>
  <svg class="abs support-label" viewBox="0 0 487 222" preserveAspectRatio="none"><polygon points="0,0 487,0 395,222 0,222" fill="#0c2b5e"/></svg>
  <div class="abs support-text">THE SUPPORT YOU<br>NEED TO MAKE THE<br><span class="big">RIGHT CHOICE</span></div>

  <div class="abs feature" style="left:495px">
    <svg width="56" height="56" viewBox="0 0 56 56"><circle cx="24" cy="14" r="9" fill="#1f5fa8"/><path d="M8 50c0-11 7-18 16-18s16 7 16 18z" fill="#1f5fa8"/><path d="M40 30l8 8-4 4" stroke="#22c58a" stroke-width="3" fill="none"/></svg>
    <p>Dedicated local advisor</p>
  </div>
  <div class="abs feature" style="left:632px">
    <svg width="56" height="56" viewBox="0 0 56 56"><path d="M6 26 20 14l14 12v24H6z" fill="#1f5fa8"/><rect x="14" y="34" width="12" height="16" fill="#fff"/><path d="M34 30l10-8 10 8v20H34z" fill="#22c58a"/></svg>
    <p>Hand-picked list of communities to match your needs</p>
  </div>
  <div class="abs feature" style="left:772px">
    <svg width="56" height="56" viewBox="0 0 56 56"><rect x="12" y="4" width="32" height="46" rx="2" fill="none" stroke="#22c58a" stroke-width="3"/><text x="28" y="32" text-anchor="middle" font-family="Montserrat" font-weight="700" font-size="18" fill="#1f5fa8">$</text><path d="M18 40h20" stroke="#1f5fa8" stroke-width="3"/></svg>
    <p>Full details and pricing</p>
  </div>
  <div class="abs feature" style="left:909px">
    <svg width="56" height="56" viewBox="0 0 56 56"><rect x="6" y="10" width="44" height="40" rx="3" fill="none" stroke="#1f5fa8" stroke-width="3"/><path d="M6 20h44" stroke="#1f5fa8" stroke-width="3"/><path d="M16 5v9M40 5v9" stroke="#22c58a" stroke-width="3"/><g fill="#1f5fa8"><rect x="14" y="26" width="6" height="5"/><rect x="25" y="26" width="6" height="5"/><rect x="36" y="26" width="6" height="5"/><rect x="14" y="36" width="6" height="5"/><rect x="25" y="36" width="6" height="5"/></g></svg>
    <p>Help scheduling tours</p>
  </div>
  <div class="abs feature" style="left:1048px">
    <svg width="56" height="56" viewBox="0 0 56 56"><path d="M6 34l6-12h30l8 12v8H6z" fill="none" stroke="#1f5fa8" stroke-width="3"/><circle cx="16" cy="42" r="5" fill="#22c58a"/><circle cx="40" cy="42" r="5" fill="#22c58a"/></svg>
    <p>Move in support</p>
  </div>

  <h2 class="abs section-title how-title">How Our <span class="accent">Service</span> Works</h2>
  <div class="abs step" style="left:49px"><div class="step-photo" role="img" aria-label="Photo of a smiling advisor wearing a phone headset" style="background:linear-gradient(160deg,#f1f1f1,#c9a58c)"></div><div class="step-num">01.</div><div class="step-text">Talk with your<br>local advisor</div></div>
  <div class="abs step alt" style="left:244px"><div class="step-photo" role="img" aria-label="Photo of a caregiver talking with a senior woman" style="background:linear-gradient(160deg,#e9e2da,#b88c72)"></div><div class="step-num">02.</div><div class="step-text">Get information<br>on care options</div></div>
  <div class="abs step" style="left:438px"><div class="step-photo" role="img" aria-label="Photo of a family visiting a senior living community" style="background:linear-gradient(160deg,#d9e0d4,#7e8c74)"></div><div class="step-num">03.</div><div class="step-text">Select the<br>communities<br>to visit</div></div>
  <div class="abs step alt" style="left:630px"><div class="step-photo" role="img" aria-label="Photo of seniors relaxing together in their new home" style="background:linear-gradient(160deg,#cfd9e6,#8a7a6c)"></div><div class="step-num">04.</div><div class="step-text">Transition to<br>new home</div></div>
  <div class="abs couple-photo" role="img" aria-label="Photo of a senior couple walking arm in arm carrying a grocery bag"></div>

  <div class="abs nocost-band" role="img" aria-label="Photo of a happy senior man stretching his arms wide against a bright blue sky"></div>
  <h2 class="abs section-title nocost-title">There's <span class="accent">No Cost</span> to You</h2>
  <p class="abs nocost-text">We work with over 20,000 senior living communities. Our community partners pay us for placement services.</p>
  <div class="abs btn-call">Call 800-555-0142</div>

  <h2 class="abs section-title vet-title">Access up to $2,000 per month <span class="accent">in veteran's aid</span></h2>
  <p class="abs vet-text">We work with Veterans every day. Most veteran families do not know of a key benefit available to them and their families. It's called the Veteran's Aid and Attendance benefit. This benefit can help pay for senior living and home care.</p>
  <div class="abs btn-learn">Learn More</div>
  <div class="abs vet-photo" role="img" aria-label="Photo of a saluting soldier silhouetted against a waving flag"></div>

  <div class="abs reviews-band"></div>
  <h2 class="abs section-title reviews-title">97% of Our Customers <span class="accent">Recommend Our Service</span></h2>
  <blockquote class="quote quote-a">Lorem ipsum dolor sit amet, consectetur adipiscing elit, sed do eiusmod tempor incididunt ut labore et dolore magna aliqua. Ut enim ad minim veniam, quis nostrud exercitation ullamco laboris nisi ut aliquip ex. Duis aute irure dolor in reprehenderit in voluptate velit esse.</blockquote>
  <blockquote class="quote quote-b">Lorem ipsum dolor sit amet, consectetur adipiscing elit, sed do eiusmod tempor incididunt ut labore et dolore magna aliqua. Ut enim ad minim veniam, quis nostrud exercitation ullamco laboris nisi ut aliquip ex. Duis aute irure dolor in reprehenderit in voluptate velit esse.</blockquote>
  <div class="abs reviewer" style="left:107px;top:2743px"><span class="avatar" role="img" aria-label="Portrait photo of the reviewer"></span><span class="reviewer-name">Margaret Ellison</span></div>
  <div class="abs reviewer" style="left:608px;top:2800px"><span class="avatar" role="img" aria-label="Portrait photo of the reviewer" style="background:linear-gradient(160deg,#efe2d3,#c5a585)"></span><span class="reviewer-name">Joanna Whitfield</span></div>
  <div class="abs dots"><span class="on"></span><span></span><span></span><span></span></div>

  <div class="abs advisor-photo" role="img" aria-label="Photo of a smiling elderly woman embraced by a younger caregiver"></div>
  <h2 class="abs section-title advisor-title">Your local advisor.<br><span class="accent">You decide.</span></h2>
  <p class="abs advisor-text">Over 400 senior advisors across the U.S. and Canada are ready to help your family with:</p>
  <ul class="abs advisor-list">
    <li><svg width="22" height="24" viewBox="0 0 22 24"><path d="M11 1a8 8 0 0 0-8 8c0 6 8 14 8 14s8-8 8-14a8 8 0 0 0-8-8z" fill="none" stroke="#0c2b5e" stroke-width="2"/><circle cx="11" cy="9" r="3" fill="#0c2b5e"/></svg>Insider's tips for the area near you</li>
    <li><svg width="24" height="24" viewBox="0 0 24 24"><circle cx="7" cy="7" r="4" fill="none" stroke="#0c2b5e" stroke-width="2"/><circle cx="17" cy="17" r="4" fill="none" stroke="#0c2b5e" stroke-width="2"/><path d="M10 10l4 4" stroke="#0c2b5e" stroke-width="2"/></svg>Advice tailored to your unique situation</li>
    <li><svg width="24" height="24" viewBox="0 0 24 24"><circle cx="12" cy="12" r="10" fill="none" stroke="#0c2b5e" stroke-width="2"/><path d="M12 10v7" stroke="#0c2b5e" stroke-width="2"/><circle cx="12" cy="7" r="1.3" fill="#0c2b5e"/></svg>Time saving know-how and resources</li>
  </ul>

  <h2 class="abs section-title states-title">Senior living <span class="accent">by state</span></h2>
  <div class="care-tab active" style="top:3733px"><span class="tab-icon"><svg width="22" height="22" viewBox="0 0 22 22"><circle cx="11" cy="5" r="3" fill="#fff"/><path d="M6 20v-8h10v8z" fill="#fff"/></svg></span>Assisted Living<span class="tab-caret"><svg width="8" height="12" viewBox="0 0 8 12"><path d="M8 0v12L0 6z" fill="#22c58a"/></svg></span></div>
  <div class="care-tab" style="top:3793px"><span class="tab-icon"><svg width="22" height="22" viewBox="0 0 22 22"><circle cx="11" cy="11" r="8" fill="none" stroke="#fff" stroke-width="2"/><path d="M7 11h8M11 7v8" stroke="#fff" stroke-width="2"/></svg></span>Memory Care</div>
  <div class="care-tab" style="top:3852px"><span class="tab-icon"><svg width="22" height="22" viewBox="0 0 22 22"><circle cx="11" cy="4" r="3" fill="#fff"/><path d="M8 21l1-9-2 3M13 21l-1-9 3 3" stroke="#fff" stroke-width="2" fill="none"/></svg></span>Independent Living</div>
  <div class="care-tab" style="top:3911px"><span class="tab-icon"><svg width="22" height="22" viewBox="0 0 22 22"><path d="M2 11 11 3l9 8v9H2z" fill="#fff"/><path d="M9 14h4M11 12v4" stroke="#0c2b5e" stroke-width="2"/></svg></span>Nursing Home</div>
  <div class="care-tab" style="top:3971px"><span class="tab-icon"><svg width="22" height="22" viewBox="0 0 22 22"><path d="M11 19s-8-5-8-10a4 4 0 0 1 8-1 4 4 0 0 1 8 1c0 5-8 10-8 10z" fill="#fff"/></svg></span>Care Homes</div>

  <ul class="state-col" style="left:450px">
    <li>Alabama</li><li>Arizona</li><li>Arkansas</li><li>California</li><li>Colorado</li><li>Connecticut</li><li>Delaware</li><li>District of Columbia</li><li>Florida</li><li>Georgia</li><li>Hawaii</li><li>Idaho</li><li>Illinois</li><li>Indiana</li><li>Iowa</li><li>Kansas</li><li>Kentucky</li>
  </ul>
  <ul class="state-col" style="left:697px">
    <li>Louisiana</li><li>Maine</li><li>Maryland</li><li>Massachusetts</li><li>Michigan</li><li>Minnesota</li><li>Mississippi</li><li>Missouri</li><li>Montana</li><li>Nebraska</li><li>Nevada</li><li>New Hampshire</li><li>New Jersey</li><li>New Mexico</li><li>New York</li><li>North Carolina</li><li>North Dakota</li>
  </ul>
  <ul class="state-col" style="left:910px">
    <li>Ohio</li><li>Oklahoma</li><li>Oregon</li><li>Pennsylvania</li><li>Rhode Island</li><li>South Carolina</li><li>South Dakota</li><li>Tennessee</li><li>Texas</li><li>Utah</li><li>Vermont</li><li>Virginia</li><li>Washington</li><li>West Virginia</li><li>Wisconsin</li><li>Wyoming</li>
  </ul>

  <footer>
    <div class="abs footer-band"></div>
    <div class="abs footer-photo" role="img" aria-label="Photo of a cheerful senior man with glasses and a cardigan"></div>
    <div class="abs footer-about">
      <div class="footer-heading">ABOUT KINDRED HARBOR NETWORK</div>
      <p>Kindred Harbor Network connects families with trusted local advisors who help compare senior living options, schedule tours and plan a calm, confident move at no cost to you.</p>
    </div>
    <div class="abs footer-links">
      <div class="footer-heading">QUICK LINKS</div>
      <ul><li>Assisted Living</li><li>Memory Care</li><li>Nursing Home</li><li>More Living Options</li><li>Planning &amp; Advice</li><li>How Our Service Works</li></ul>
    </div>
    <svg class="abs footer-panel" viewBox="0 0 338 304" preserveAspectRatio="none"><polygon points="40,0 338,0 338,304 0,304 0,60" fill="#0c2b5e"/></svg>
    <div class="abs footer-brand"><span class="brand-dot"></span><span class="brand-name">Kindred Harbor Network</span></div>
    <div class="abs footer-phone">
      <span class="phone-ring"><svg width="22" height="22" viewBox="0 0 24 24"><path d="M6.6 10.8a15 15 0 0 0 6.6 6.6l2.2-2.2a1 1 0 0 1 1-.25 11.4 11.4 0 0 0 3.6.57 1 1 0 0 1 1 1V20a1 1 0 0 1-1 1A17 17 0 0 1 3 4a1 1 0 0 1 1-1h3.5a1 1 0 0 1 1 1c0 1.25.2 2.45.57 3.57a1 1 0 0 1-.25 1z" fill="#fff"/></svg></span>
      <div><div class="phone-number">1-800-555-0142</div><div class="phone-note">Talk Today to a Local Advisor for FREE</div></div>
    </div>
    <div class="abs copyright">COPYRIGHT © 2019 KINDRED HARBOR NETWORK. ALL RIGHTS RESERVED.</div>
  </footer>

</div>
</body>
</html>
```